BrambleWare business card

Looking for business card design that supports our company/software values. We have 2 logo designs at the moment but open to change if you think you can enhance the brand. Check out website www.brambleware.com.au.

Target Market(s)

Education

Contact Information for Business Card

Name, title, mobile, email and website

Font styles to use
Sans Serif

Colors

Designer to choose colors to be used in the design.

Requirements
Must have
• BrambleWare logo with tree and tagline on rear side with dark grey background colour

```html
<!DOCTYPE html>
<html lang="en">
<head>
<meta charset="utf-8">
<title>BrambleWare business card</title>
<link rel="stylesheet" href="https://fonts.googleapis.com/css2?family=Montserrat:wght@400;500;700&family=Open+Sans:wght@400;600&display=swap">
<style>
  :root {
    --stage: #b9bbbc;
    --charcoal: #4e504d;
    --sunflower: #fbb934;
    --paper: #ffffff;
    --leaf: #3c7a2a;
    --ink: #3f403e;
    --muted: #dcdcdc;
  }
  * { box-sizing: border-box; margin: 0; padding: 0; }
  html, body { width: 1200px; height: 800px; overflow: hidden; }
  body {
    background: var(--stage);
    position: relative;
    font-family: "Open Sans", sans-serif;
  }
  .card {
    position: absolute;
    width: 620px;
    height: 340px;
    overflow: hidden;
    box-shadow: 0 6px 18px rgba(0,0,0,0.25);
  }
  /* Rear side */
  .card-back { left: 380px; top: 40px; background: var(--charcoal); }
  .card-back .figure-area {
    position: absolute; left: 0; top: 0; width: 230px; height: 100%;
    background: linear-gradient(160deg, #fcc24a 0%, var(--sunflower) 70%);
    border-radius: 0 140px 0 0;
  }
  .card-back .lockup {
    position: absolute; left: 300px; top: 150px; color: var(--paper);
  }
  .brand-name {
    font-family: "Open Sans", sans-serif;
    font-weight: 600;
    font-size: 40px;
    letter-spacing: 0.5px;
    line-height: 1;
    display: flex; align-items: center; gap: 12px;
  }
  .brand-dot { width: 14px; height: 14px; border-radius: 50%; background: currentColor; flex: none; }
  .tagline {
    font-size: 15px; letter-spacing: 0.6px;
    border-top: 1px solid currentColor;
    margin-top: 8px; padding-top: 4px; padding-left: 26px;
  }
  .card-back .web {
    position: absolute; left: 340px; top: 268px;
    color: var(--paper); font-size: 14px; letter-spacing: 2.5px;
  }
  /* Front side */
  .card-front { left: 180px; top: 420px; background: var(--paper); }
  .card-front .figure-area {
    position: absolute; right: 0; top: 0; width: 200px; height: 100%;
    background: linear-gradient(200deg, var(--charcoal) 0%, var(--charcoal) 80%, var(--sunflower) 100%);
    border-radius: 120px 0 0 0;
  }
  .card-front .lockup {
    position: absolute; left: 40px; top: 40px; color: var(--ink);
  }
  .card-front .brand-name { font-size: 34px; }
  .card-front .tagline { font-size: 13px; }
  .person { position: absolute; left: 50px; top: 160px; font-family: "Montserrat", sans-serif; }
  .person-name { color: var(--leaf); font-weight: 700; font-size: 20px; }
  .person-title { color: var(--ink); font-size: 15px; margin-top: 2px; }
  .contacts { list-style: none; position: absolute; left: 50px; top: 232px; font-family: "Montserrat", sans-serif; color: var(--ink); font-size: 15px; }
  .contacts li { display: flex; align-items: center; gap: 8px; height: 22px; }
  .contacts svg { width: 15px; height: 15px; flex: none; }
</style>
</head>
<body>
  <section class="card card-back" aria-label="Card rear side">
    <div class="figure-area" role="img" aria-label="Large yellow stylised figure with raised arms"></div>
    <div class="lockup">
      <div class="brand-name"><span class="brand-dot"></span>BrambleWare</div>
      <div class="tagline">Student Success Platform</div>
    </div>
    <div class="web">www.brambleware.com.au</div>
  </section>

  <section class="card card-front" aria-label="Card front side">
    <div class="lockup">
      <div class="brand-name"><span class="brand-dot"></span>BrambleWare</div>
      <div class="tagline">Student Success Platform</div>
    </div>
    <div class="person">
      <div class="person-name">Daniel Hartley</div>
      <div class="person-title">President</div>
    </div>
    <ul class="contacts">
      <li>
        <svg viewBox="0 0 16 16" fill="none" stroke="#3c7a2a" stroke-width="1.5"><rect x="4" y="1" width="8" height="14" rx="1.5"/><line x1="7" y1="12.5" x2="9" y2="12.5"/></svg>
        +61 412 345 678
      </li>
      <li>
        <svg viewBox="0 0 16 16" fill="none" stroke="#3c7a2a" stroke-width="1.5"><rect x="1" y="3" width="14" height="10"/><polyline points="1,3 8,9 15,3"/></svg>
        daniel@brambleware.com.au
      </li>
      <li>
        <svg viewBox="0 0 16 16" fill="none" stroke="#3c7a2a" stroke-width="1.3"><circle cx="8" cy="8" r="6.5"/><ellipse cx="8" cy="8" rx="3" ry="6.5"/><line x1="1.5" y1="8" x2="14.5" y2="8"/></svg>
        www.brambleware.com.au
      </li>
    </ul>
    <div class="figure-area" role="img" aria-label="Large grey stylised figure with raised arm and yellow accent"></div>
  </section>
</body>
</html>
```